Ferrobolt Anchor Clamp Brochure

We need a brochure to promote a brand new patented product. The product is a lock that ensure a shipping container itself cannot be stolen as even though you can stop someone breaking into a shipping container up until now you could not stop them from simply stealing the entire container using a crane/hyab truck/tilt tray truck/etc. This product is therefore all about security of the high value items with the container. The lock works in conjunction with standard shipping container 'twist locks'.
We would like our logo within the design. We can supply more images of required as this product is 3D modeled so you need only ask.

```html
<!DOCTYPE html>
<html lang="en">
<head>
<meta charset="utf-8">
<title>Ferrobolt Anchor Clamp Brochure</title>
<link href="https://fonts.googleapis.com/css2?family=Lato:wght@400;700&display=swap" rel="stylesheet">
<style>
  :root {
    --stage: #dcdcdc;
    --blue-light: #1ba9e8;
    --blue-mid: #1577c4;
    --blue-deep: #0b3f82;
    --header-band: rgba(236, 239, 243, 0.94);
    --ink-dark: #1c1c1c;
    --text-light: #ffffff;
    --thumb-border: #e8eef4;
  }
  * { box-sizing: border-box; margin: 0; padding: 0; }
  html, body { width: 1200px; height: 796px; overflow: hidden; }
  body {
    background: var(--stage);
    font-family: "Lato", sans-serif;
    position: relative;
  }
  .brochure {
    position: absolute;
    left: 375px; top: 55px;
    width: 465px; height: 662px;
    background: linear-gradient(180deg, var(--blue-light) 0%, var(--blue-mid) 45%, var(--blue-deep) 100%);
    color: var(--text-light);
    overflow: hidden;
  }
  .headline-band {
    position: absolute;
    left: 13px; top: 15px;
    width: 439px; height: 98px;
    background: var(--header-band);
    display: flex; align-items: center; justify-content: center;
    text-align: center;
  }
  .headline {
    color: var(--ink-dark);
    font-weight: 400;
    font-size: 25px;
    line-height: 29px;
    letter-spacing: -0.2px;
  }
  .headline strong { font-weight: 700; }
  .hero-photo {
    position: absolute;
    left: 13px; top: 113px;
    width: 439px; height: 172px;
    background: linear-gradient(180deg, #9aa5b0 0%, #c4ccd3 45%, #a4433f 72%, #5a4f49 100%);
  }
  .thumbnails {
    position: absolute;
    left: 27px; top: 283px;
    width: 411px;
    display: flex; justify-content: space-between;
  }
  .thumb {
    width: 95px; height: 60px;
    border: 2px solid var(--thumb-border);
    box-shadow: 0 2px 4px rgba(0,0,0,0.35);
  }
  .thumb-red { background: linear-gradient(135deg, #b86a6a, #8e4646); }
  .thumb-grey { background: linear-gradient(135deg, #9ea4aa, #5e656c); }
  .thumb-white { background: linear-gradient(135deg, #ffffff, #d4d8dc); }
  .body-copy {
    position: absolute;
    left: 31px; top: 353px;
    width: 403px;
    text-align: center;
  }
  .body-copy p { margin-bottom: 5px; }
  .lead { font-size: 10.6px; line-height: 13.6px; }
  .detail { font-size: 8px; line-height: 10.6px; }
  .contact-bar {
    position: absolute;
    left: 24px; top: 605px;
    width: 425px; height: 48px;
    display: flex; align-items: flex-start;
  }
  .contact-col { margin-right: 14px; }
  .contact-col h3 {
    font-size: 12px; font-weight: 400;
    display: flex; align-items: center; gap: 5px;
    margin-bottom: 4px;
  }
  .contact-col h3 svg { width: 12px; height: 12px; }
  .contact-col p { font-size: 8.4px; line-height: 11px; }
  .col-phone { width: 66px; }
  .col-address { width: 116px; }
  .col-web { width: 82px; margin-right: 0; }
  .brand {
    margin-left: 14px;
    height: 48px;
    display: flex; align-items: center;
    color: var(--text-light);
    font-weight: 700;
    font-size: 26px;
    letter-spacing: 1px;
  }
</style>
</head>
<body>
  <main class="brochure">
    <header class="headline-band">
      <h1 class="headline">MAKE YOUR CONTAINER <strong>SECURE</strong><br>WITH OUR <strong>TWIST LOCKS!</strong></h1>
    </header>

    <div class="hero-photo" role="img" aria-label="Photograph of a container port with green gantry cranes, stacked red and blue shipping containers and a ship under a cloudy sky"></div>

    <div class="thumbnails">
      <div class="thumb thumb-red" role="img" aria-label="Render of the clamp fitted to a red container corner"></div>
      <div class="thumb thumb-grey" role="img" aria-label="Render of a red twist lock mechanism"></div>
      <div class="thumb thumb-red" role="img" aria-label="Close-up render of the clamp installed in a container corner casting"></div>
      <div class="thumb thumb-white" role="img" aria-label="Render of the stainless steel clamp and bolt"></div>
    </div>

    <section class="body-copy">
      <p class="lead">Your shipping container can be easily locked securely shut, but what is stopping someone from simply picking up the entire container and stealing it with all your belongings inside? We have developed a patented locking system that allows you to easily lock your shipping container to footings or to another shipping container if you are multiple stacking.</p>
      <p class="detail">Our shipping container locks ensure your container is safe from theft by any means. It ensures your container cannot be removed from it's footings by anyone but the owner. If you need security in a shipping container yard simple use the lock to connect and lock two shipping containers together vertically. It is impossible for double stacked shipping containers to be transported due to their height even if they can be picked up!</p>
      <p class="lead">The lock is easily installed and removed in a matter of seconds, they are available individually keyed or keyed alike and are manufactured in Stainless Steel.</p>
      <p class="detail">How does it work? Our patented design works in conjunction with a standard double ended, weldable or boltable twist lock in a way that ensures the twist lock cannot be opened once the lock is installed.</p>
      <p class="detail">A minimum of two Ferrobolt Anchor Clamps are needed per container, located in opposite corners but we advise for maximum security four should be used, one in each corner.</p>
      <p class="lead">So, the answer as to how do you stop someone stealing your shipping container is now easily answered, simply install our Ferrobolt Anchor Clamps.</p>
    </section>

    <footer class="contact-bar">
      <div class="contact-col col-phone">
        <h3><svg viewBox="0 0 12 12"><rect width="12" height="12" rx="2" fill="#ffffff"/><path d="M3.6 2.6l1.3 1.7-.7.9c.5 1 1.4 1.9 2.4 2.4l.9-.7 1.7 1.3-.9 1.2C5.8 9.2 2.8 6.2 2.4 3.5z" fill="#1577c4"/></svg>Call Us</h3>
        <p>0400 555 182<br>02 9000 4417</p>
      </div>
      <div class="contact-col col-address">
        <h3><svg viewBox="0 0 12 12"><rect width="12" height="12" rx="2" fill="#ffffff"/><path d="M6 2.2a2.7 2.7 0 0 0-2.7 2.7C3.3 7 6 10 6 10s2.7-3 2.7-5.1A2.7 2.7 0 0 0 6 2.2zm0 3.8a1.1 1.1 0 1 1 0-2.2 1.1 1.1 0 0 1 0 2.2z" fill="#1577c4"/></svg>Our Address</h3>
        <p>58 Harbourline Way<br>Portview NSW 2999</p>
      </div>
      <div class="contact-col col-web">
        <h3><svg viewBox="0 0 12 12"><rect width="12" height="12" rx="2" fill="#ffffff"/><circle cx="6" cy="6" r="3.4" fill="none" stroke="#1577c4" stroke-width="1"/><path d="M2.6 6h6.8M6 2.6c-1.6 1.8-1.6 5 0 6.8M6 2.6c1.6 1.8 1.6 5 0 6.8" fill="none" stroke="#1577c4" stroke-width="0.8"/></svg>Contact Us</h3>
        <p>www.korva.example<br>info@korva.example</p>
      </div>
      <div class="brand">Korva</div>
    </footer>
  </main>
</body>
</html>
```